Delbert Finchley Political Campaign Business Cards

Design business card that encorporated Texas Halbrook Parish and my existing campaign. Somewhere on the card needs to have. Halbrook Parish is in Texas and I am running for Halbrook Parish Judge. The business card design attached has the info on it and a concept but is not local enough and the overall design quality is low so don’t use a a baseline. Not looking for modern anything, should have square for corners, running for Halbrook Parish Judge.

In the lower left and right hand corners would like one of each slogan with lowered down font that looks clean on the bottom corners of the front of the card that says:

“Retired Staff Sergeant Coastal Federal Militia”
“KSV/KPD Veteran”

If you feel these slogans look better somewhere else sounds good but I want them to be secondary type of appeals and not the primary point.

Phone we can incorporate in as well:
555-302-4819

Facebook:
www.Pagebuzz.com/shiftbrenor

Website:
www.steadfastmarbleridge.com

County website:

https://www.halbrookparish.gov/Pages/default.aspx

Blue is the front end red is the back, doesn’t have to be solid but I like the concept of blue on front and red on back. Not absolutely necessary if doesn’t fit design and what looks best.

Eliminate the phrase Conservative Democrat from the project

Two photos have been added to replace the KPD/KSV text. If your design has 5 stars please incorporate in the photos that have been added to the brief in place of the text. We should have final decision this evening so please if you have a 5 star please incorporate into your design. If the background color needs to change to make it work sounds good

Industry/Entity Type

Political

Contact Information for Business Card

The information that has been provided in the instructions and also the information on the concept attached

Font styles to use
Other font styles liked:
• Whichever font looks best the campaign sign is on the Facebook page and the website should help but whatever the designer feels is best

Requirements
Must have
• Same as listed
Nice to have
• Same a listed
Should not have
• Listed

```html
<!DOCTYPE html>
<html lang="en">
<head>
<meta charset="utf-8">
<title>Delbert Finchley for Halbrook Parish Judge – Business Cards</title>
<link rel="stylesheet" href="https://fonts.googleapis.com/css2?family=Saira+Semi+Condensed:wght@600;700&display=swap">
<style>
  :root {
    --backdrop: #6e5843;
    --front-blue: #233d93;
    --back-red: #c41f2c;
    --ink-white: #ffffff;
    --star-blush: #f2c4b4;
    --seal-tint: rgba(190, 170, 230, 0.22);
    --seal-edge: rgba(20, 30, 90, 0.35);
  }
  html, body {
    margin: 0;
    width: 900px;
    height: 1200px;
    overflow: hidden;
    background: var(--backdrop);
  }
  .canvas {
    position: relative;
    width: 900px;
    height: 1200px;
    font-family: "Saira Semi Condensed", "Arial Narrow", sans-serif;
    font-weight: 700;
    color: var(--ink-white);
    font-variant: small-caps;
  }
  .card {
    position: absolute;
    width: 773px;
    height: 444px;
    overflow: hidden;
  }
  .card--front { left: 72px; top: 136px; background: var(--front-blue); }
  .card--back  { left: 74px; top: 624px; background: var(--back-red); }

  .star-row { position: absolute; display: flex; gap: 4px; }
  .star-row svg { width: 22px; height: 22px; display: block; }
  .card--front .star-row svg { fill: var(--ink-white); }
  .card--back .star-row svg { fill: var(--star-blush); }
  .star-row--tl { left: 35px; top: 38px; }
  .star-row--tr { right: 35px; top: 38px; }
  .card--back .star-row--tl, .card--back .star-row--tr { top: 35px; }
  .star-row--bl { left: 35px; bottom: 34px; }
  .star-row--br { right: 35px; bottom: 34px; }

  .county-seal {
    position: absolute;
    left: 383px;
    top: 35px;
    width: 410px;
    height: 410px;
    border-radius: 50%;
    background: var(--seal-tint);
    border: 3px solid var(--seal-edge);
    box-sizing: border-box;
  }

  .candidate {
    position: absolute;
    left: 0; right: 0;
    top: 128px;
    text-align: center;
    margin: 0;
    font-weight: 700;
  }
  .candidate__name {
    display: block;
    font-size: 70px;
    line-height: 1;
    letter-spacing: 1px;
  }
  .candidate__for {
    display: flex;
    align-items: center;
    justify-content: center;
    gap: 14px;
    font-size: 32px;
    font-style: italic;
    font-weight: 600;
    font-variant: normal;
    line-height: 1;
    margin-top: 10px;
  }
  .candidate__for::before, .candidate__for::after {
    content: "";
    width: 104px;
    height: 2px;
    background: var(--ink-white);
  }
  .candidate__office {
    display: block;
    font-size: 54px;
    line-height: 1;
    margin-top: 6px;
  }

  .credential {
    position: absolute;
    bottom: 36px;
    font-size: 20px;
    line-height: 1;
    letter-spacing: 0.3px;
    margin: 0;
    white-space: nowrap;
  }
  .credential--service { left: 35px; }
  .credential--tour { right: 35px; }

  .contact {
    position: absolute;
    left: 0; right: 0;
    top: 133px;
    margin: 0;
    padding: 0;
    list-style: none;
    text-align: center;
    font-size: 22px;
    line-height: 30px;
  }
  .contact li {
    display: flex;
    align-items: center;
    justify-content: center;
    gap: 8px;
    white-space: nowrap;
  }
  .contact svg { width: 22px; height: 22px; fill: none; stroke: var(--ink-white); stroke-width: 2; }
  .contact .icon-solid { fill: var(--ink-white); stroke: none; }
  .contact__divider {
    width: 86px;
    height: 2px;
    background: var(--ink-white);
    margin: 15px auto 20px;
  }
  .social-dot {
    width: 22px; height: 22px;
    border-radius: 50%;
    background: var(--ink-white);
  }
</style>
</head>
<body>
<svg width="0" height="0" style="position:absolute">
  <defs>
    <symbol id="star" viewBox="0 0 24 24">
      <path d="M12 1.5l3.1 7.1 7.7.7-5.8 5.1 1.7 7.6L12 18l-6.7 4 1.7-7.6L1.2 9.3l7.7-.7z"/>
    </symbol>
  </defs>
</svg>

<main class="canvas">
  <section class="card card--front" aria-label="Card front">
    <div class="county-seal" role="img" aria-label="Faint parish emblem circle"></div>

    <div class="star-row star-row--tl"><svg><use href="#star"/></svg><svg><use href="#star"/></svg><svg><use href="#star"/></svg><svg><use href="#star"/></svg><svg><use href="#star"/></svg></div>
    <div class="star-row star-row--tr"><svg><use href="#star"/></svg><svg><use href="#star"/></svg><svg><use href="#star"/></svg><svg><use href="#star"/></svg><svg><use href="#star"/></svg></div>

    <h1 class="candidate">
      <span class="candidate__name">Delbert Finchley</span>
      <span class="candidate__for">for</span>
      <span class="candidate__office">Halbrook Parish Judge</span>
    </h1>

    <p class="credential credential--service">Retired Staff Sergeant Coastal Federal Militia</p>
    <p class="credential credential--tour">KSV/KPD Veteran</p>
  </section>

  <section class="card card--back" aria-label="Card back">
    <div class="star-row star-row--tl"><svg><use href="#star"/></svg><svg><use href="#star"/></svg><svg><use href="#star"/></svg><svg><use href="#star"/></svg><svg><use href="#star"/></svg></div>
    <div class="star-row star-row--tr"><svg><use href="#star"/></svg><svg><use href="#star"/></svg><svg><use href="#star"/></svg><svg><use href="#star"/></svg><svg><use href="#star"/></svg></div>

    <ul class="contact">
      <li>
        <svg viewBox="0 0 24 24" class="icon-solid"><path d="M6.6 10.8a15.1 15.1 0 0 0 6.6 6.6l2.2-2.2c.3-.3.7-.4 1-.2 1.1.4 2.3.6 3.6.6.6 0 1 .4 1 1V20c0 .6-.4 1-1 1A17 17 0 0 1 3 4c0-.6.4-1 1-1h3.5c.6 0 1 .4 1 1 0 1.3.2 2.5.6 3.6.1.3 0 .7-.2 1z"/></svg>
        555-302-4819
      </li>
      <li>
        <svg viewBox="0 0 24 24"><circle cx="12" cy="12" r="9.5"/><ellipse cx="12" cy="12" rx="4" ry="9.5"/><path d="M2.5 12h19M4 7h16M4 17h16"/></svg>
        www.steadfastmarbleridge.com
      </li>
      <li>
        <svg viewBox="0 0 24 24" class="icon-solid"><path d="M2 5h20v14H2z"/><path d="M3 6l9 7 9-7" fill="none" stroke="#c41f2c" stroke-width="1.6"/></svg>
        delbert@steadfastmarbleridge.com
      </li>
      <li class="contact__divider" aria-hidden="true"></li>
      <li>
        <span class="social-dot" aria-hidden="true"></span>
        www.Pagebuzz.com/shiftbrenor
      </li>
      <li>
        <svg viewBox="0 0 24 24"><circle cx="12" cy="12" r="9.5"/><ellipse cx="12" cy="12" rx="4" ry="9.5"/><path d="M2.5 12h19M4 7h16M4 17h16"/></svg>
        www.halbrookparish.gov/Pages/default.aspx
      </li>
    </ul>

    <div class="star-row star-row--bl"><svg><use href="#star"/></svg><svg><use href="#star"/></svg><svg><use href="#star"/></svg><svg><use href="#star"/></svg><svg><use href="#star"/></svg></div>
    <div class="star-row star-row--br"><svg><use href="#star"/></svg><svg><use href="#star"/></svg><svg><use href="#star"/></svg><svg><use href="#star"/></svg><svg><use href="#star"/></svg></div>
  </section>
</main>
</body>
</html>
```